KWM Compliant Dietary Supplement Label for Nutritional Company

We are in need of a label for our line of 20+ dietary supplements that are specifically formulated to balance body chemistry and match the biochemical individuality of our users based on hair tissue mineral analysis.

We have a line of approximately 20 different dietary supplements that will require use of new label in both a small (90 capsule) and large (180 capsule) size. We will start with the initial label in which Product name, Supplement Facts, and Ingredient list will need to be modified for each particular product thereafter.

The label will be placed on a transparent blue bottle with the color of lid being decided after label design. We are open to a transparent light amber bottle with black lid but blue is our preference.

We would like the majority of the label to be blue. Solid blue, fading of blue to darker blue/black, or subtle background designs are welcome with involvement of white and hints of orange. We do not want pictorial images on the label.

Label size:
Small bottle (120cc): Label size ~ 2.25” x 5.875”
Large bottle (200cc): Label size ~ 2.75” x 7.625”

Front:
-Logo near top of label with product name and description in middle and capsule count near the bottom

Right Side:
-Supplement Facts: See current product image below in brief
-Ingredient list: See current product image below in brief
-Manufactured for: See image below (This is on the left side of our current bottle and would like it moved to the bottom of the right side)

Left side:
-Suggested use: See current product image below in brief
-Leave room for possible warning statement
-Leave room for possible lot number printing
-Keep out of the reach of children.

The first files below are our current supplement label with product information. This information is what is needed on the label and will likely need some adjustments as we are updating our line of supplements and changes in KWM requirements.

The following files are the logo files and color palette.

The remaining files are some designs we came across for inspiration.

Thank you.

Target Market(s)

Health Care Profressionals

Industry/Entity Type

Health Care and Nutrition

Requirements
Nice to have
• Product name needs to be on same line in all one color
Should not have
• Pictorial Images

```html
<!DOCTYPE html>
<html lang="en">
<head>
<meta charset="utf-8">
<title>Adreva Adrenal Supplement – Label</title>
<link href="https://fonts.googleapis.com/css2?family=Poppins:wght@400;500;600;700;800&family=Oswald:wght@600;700&family=Montserrat:wght@400;500;600&display=swap" rel="stylesheet">
<style>
  :root{
    --canvas:#b0b0b0;
    --label-bg:#03060f;
    --band:#1d3a75;
    --rule:#8a8f99;
    --orange:#f5821f;
    --brand-blue:#3567b8;
    --white:#ffffff;
  }
  *{box-sizing:border-box;margin:0;padding:0}
  html,body{width:957px;height:1200px;overflow:hidden;background:var(--canvas)}
  body{position:relative;font-family:"Poppins",sans-serif;color:var(--white)}

  .label{position:absolute;left:28px;top:428px;width:900px;height:344px;background:var(--label-bg);overflow:hidden}
  .band-top{position:absolute;left:0;top:0;width:100%;height:18px;background:var(--band)}
  .rule-bottom{position:absolute;left:0;top:320px;width:100%;height:5px;background:var(--rule)}
  .band-bottom{position:absolute;left:0;top:326px;width:100%;height:18px;background:var(--band)}

  /* left panel */
  .info-block{position:absolute;left:19px;width:187px}
  .info-tab{display:inline-block;background:var(--orange);color:var(--white);font-weight:700;font-size:9.5px;padding:1px 8px 0 8px;border-radius:4px 4px 0 0;letter-spacing:.2px;line-height:13px}
  .info-box{border:1.3px solid var(--white);border-radius:4px;height:40px;padding:7px 7px;font-size:7px;line-height:8.5px}
  .use{top:44px}.warn-1{top:113px}.warn-2{top:255px}

  /* front panel */
  .brand{position:absolute;left:340px;top:88px;width:218px;text-align:center}
  .brand-name{font-family:"Montserrat",sans-serif;font-weight:500;font-size:25px;color:var(--brand-blue);letter-spacing:1px;line-height:30px}
  .brand-dot{display:inline-block;width:10px;height:10px;border-radius:50%;background:var(--orange);margin-left:4px;vertical-align:4px}
  .brand-sub{font-family:"Montserrat",sans-serif;font-size:9px;letter-spacing:4.6px;color:var(--white);margin-top:2px}
  .product-name{position:absolute;left:300px;top:146px;width:298px;text-align:center;font-family:"Oswald",sans-serif;font-weight:700;font-size:52px;line-height:60px;color:var(--brand-blue);letter-spacing:1px}
  .product-desc{position:absolute;left:340px;top:210px;width:216px;height:29px;border:1.5px solid var(--white);text-align:center;font-family:"Montserrat",sans-serif;font-weight:600;font-size:11.5px;letter-spacing:3.6px;line-height:26px}
  .dietary{position:absolute;left:322px;top:300px;font-family:"Montserrat",sans-serif;font-size:8px;letter-spacing:2.4px;color:var(--orange)}
  .count{position:absolute;left:480px;top:258px;display:flex;align-items:flex-end}
  .count-num{font-family:"Oswald",sans-serif;font-weight:700;font-size:46px;line-height:52px;color:var(--orange)}
  .count-unit{font-weight:700;font-size:10.5px;margin:0 0 9px 3px}

  /* right panel */
  .facts{position:absolute;left:707px;top:29px;width:180px;height:213px;border:1.5px solid var(--white);padding:3px 5px;font-size:5px;line-height:6px}
  .facts-title{font-weight:800;font-size:18px;line-height:18px;letter-spacing:-.4px}
  .facts-meta{font-size:4.6px;line-height:5px;font-weight:600}
  .facts-bar{height:3px;background:var(--white);margin:3px 0 2px}
  .facts-head,.facts-row{display:grid;grid-template-columns:1fr 40px 26px;align-items:end}
  .facts-head{font-size:4.6px;line-height:5px;text-align:right;padding-bottom:2px;border-bottom:.8px solid var(--white)}
  .facts-row{border-bottom:.8px solid var(--white);padding:2px 0 1px;min-height:11px}
  .facts-row .amt{font-size:7.5px;line-height:8px}
  .facts-row .dv{font-size:6.5px;line-height:8px;text-align:right}
  .facts-row.compact{min-height:8px;padding:1px 0 0}
  .facts-row.compact .amt{font-size:7px}
  .facts-bar.thin{height:2px;margin:2px 0 1px}
  .facts-note{font-size:4.6px;font-weight:600;margin-top:2px}

  .ingredients{position:absolute;right:13px;top:252px;text-align:right;font-size:7px;line-height:7.8px}
  .section-title{color:var(--orange);font-weight:700;font-size:7.5px;line-height:9px}
  .made-for{position:absolute;right:13px;top:285px;text-align:right;font-size:6px;line-height:7px}
  .made-for strong{font-weight:700}
</style>
</head>
<body>
  <section class="label" aria-label="Adreva adrenal supplement label">
    <div class="band-top"></div>

    <div class="info-block use">
      <span class="info-tab">SUGGESTED USE</span>
      <div class="info-box">One capsule daily as directed by a physician</div>
    </div>
    <div class="info-block warn-1">
      <span class="info-tab">WARNING</span>
      <div class="info-box"></div>
    </div>
    <div class="info-block warn-2">
      <span class="info-tab">WARNING</span>
      <div class="info-box">IT is advisable to keep this and all supplements out of the reach of children.</div>
    </div>

    <div class="brand">
      <div class="brand-name">VARROW<span class="brand-dot"></span></div>
      <div class="brand-sub">LABORATORIES</div>
    </div>
    <h1 class="product-name">ADREVA</h1>
    <div class="product-desc">ADRENAL SUPPLEMENT</div>
    <div class="dietary">DIETARY SUPPLEMENT</div>
    <div class="count"><span class="count-num">90</span><span class="count-unit">CAPSULES</span></div>

    <div class="facts">
      <div class="facts-title">NUTRITION FACTS</div>
      <div class="facts-meta">SERVING SIZE: 1 capsule<br>SERVING PER CONTAINER : 90</div>
      <div class="facts-bar"></div>
      <div class="facts-head"><span></span><span>AMOUNT<br>PER SERVING</span><span>% daily<br>value</span></div>
      <div class="facts-row"><span>VITAMIN C ( as carbolic acid)</span><span class="amt">100mg</span><span class="dv">111%</span></div>
      <div class="facts-row"><span>VITAMIN B5<br>(as D-calcium pantothenate)</span><span class="amt">100mg</span><span class="dv">2000%</span></div>
      <div class="facts-row"><span>MAGNESIUM<br>(as magnesium amino acid chelate)</span><span class="amt">5mg</span><span class="dv">1%</span></div>
      <div class="facts-row"><span>ZINC (as zinc amino acid chelate)</span><span class="amt">1mg</span><span class="dv">9%</span></div>
      <div class="facts-row"><span>MANGANESE<br>(as manganese amino acid chelate)</span><span class="amt">1mg</span><span class="dv">43%</span></div>
      <div class="facts-row"><span>POTASSIUM<br>(as potassium amino acid chelate)</span><span class="amt">25mg</span><span class="dv">1%</span></div>
      <div class="facts-bar thin"></div>
      <div class="facts-row compact"><span>Suprarenal (adrenal) powder (bovine)</span><span class="amt">100mg</span><span class="dv">–</span></div>
      <div class="facts-row compact"><span>Liver powder, defatted (bovine)</span><span class="amt">45mg</span><span class="dv">–</span></div>
      <div class="facts-row compact"><span>Betaine Hydrochloride</span><span class="amt">25mg</span><span class="dv">–</span></div>
      <div class="facts-bar thin"></div>
      <div class="facts-note">* Daily value not established</div>
    </div>

    <div class="ingredients">
      <div class="section-title">INGREDIENTS:</div>
      Hypromellose (vegetable capsule)<br>RiceFlo (Organic rice fiber)
    </div>
    <div class="made-for">
      <div class="section-title">Manufactured for:</div>
      <strong>VARROW LABORATORIES, INC.</strong><br>Mesa Ridge, AZ 85000 USA
    </div>

    <div class="rule-bottom"></div>
    <div class="band-bottom"></div>
  </section>
</body>
</html>
```